Advertising for school programs

We're wanting some advertising material for two new programs that we are running in 2022 and 2023. The programs are:
- Summit Scholars Advancement Program
- Peak Form Sporting
Ideally we would like logos and advertising tiles for each that can be used across social media networks. It would be great to have simple advertising materials, that include the name of the program, a logo for each program, and some text that encourages people to apply.
We'd love to have designs with drawn students, so we don't have to use photos. I've included some photos and our school logo to assist.
A description of the programs is included below to help guide the design - You do not need to include ANY or ALL of the text below in the graphics, I have provided it for context.
A description of both programs below:
Summit:
The Summit Scholars Advancement Program is a differentiated pathway that caters specifically for highly capable students.
In the Summit Scholars Advancement Pathway, students can learn and be assessed at a pace exceeding that of their current year level, with a focus on 21st Century Skills.
For information about the program and application packages, please see the summit page of our website or contact Megan Tolland Head of Department Junior School mtoll41@schoolnet-example.edu.au
Peak Form Sporting:
In 2022, we will be launching the Peak Form Sporting program to cater for our highly capable athletes.
Harlow Vale has long been home to exceptional sporting talent, with multiple state and national representatives in a range of sports and year levels. Peak Form Sporting will provide a differentiated Health and Physical Education curriculum to ensure our student athletes benefit from the latest information on health, wellbeing, fitness and metal health.
The program is open to athletes from all sports and athletic pursuits, as the program is a holistic look at health and athletic performance.

```html
<!DOCTYPE html>
<html lang="en">
<head>
<meta charset="utf-8">
<title>Summit Scholars Advancement Program 2022</title>
<link rel="stylesheet" href="https://fonts.googleapis.com/css2?family=Fredoka:wght@500&family=League+Spartan:wght@700;800&family=Lexend:wght@400;500;600;700&display=swap">
<style>
  :root {
    --sky: #009fe3;
    --sun: #ffe600;
    --paper: #ffffff;
    --ink: #111111;
    --navy-text: #1d5f9e;
    --bubble: rgba(190, 230, 250, 0.55);
  }
  * { box-sizing: border-box; margin: 0; padding: 0; }
  html, body { width: 1200px; height: 1200px; overflow: hidden; background: var(--sky); }
  .poster { position: relative; width: 1200px; height: 1200px; overflow: hidden; font-family: "Lexend", sans-serif; }
  .landscape {
    position: absolute; left: 0; top: 560px; width: 1200px; height: 540px;
    background: linear-gradient(180deg, rgba(0,159,227,0) 0%, rgba(60,140,150,0.45) 40%, rgba(70,120,90,0.55) 75%, rgba(80,120,90,0.6) 100%);
  }
  .shapes { position: absolute; inset: 0; }
  .year {
    position: absolute; left: 74px; top: 40px;
    font-family: "Fredoka", sans-serif; font-weight: 500; font-size: 158px; line-height: 1;
    color: var(--sun); letter-spacing: 2px;
  }
  .title { position: absolute; left: 76px; top: 195px; color: var(--sky); font-family: "League Spartan", sans-serif; font-weight: 800; line-height: 1; }
  .title span { display: block; }
  .title .line-1 { font-size: 54px; }
  .title .line-2 { font-size: 70px; margin-top: 14px; }
  .title .line-3 { font-size: 98px; margin-top: 12px; }
  .school-name {
    position: absolute; left: 648px; top: 138px; display: flex; align-items: center; gap: 10px;
    font-family: "Lexend", sans-serif; font-weight: 700; font-size: 24px; color: var(--sky);
  }
  .school-name .dot { width: 18px; height: 18px; border-radius: 50%; background: var(--sky); }
  .lead { position: absolute; left: 76px; top: 578px; color: var(--paper); font-size: 31px; line-height: 42px; font-weight: 400; }
  .lead em, .detail em { font-style: normal; color: var(--sun); }
  .detail { position: absolute; left: 76px; top: 720px; width: 1080px; color: var(--paper); font-size: 19.5px; line-height: 27px; font-weight: 600; }
  .info-text { position: absolute; left: 76px; top: 806px; color: var(--navy-text); font-size: 20px; line-height: 26px; font-weight: 600; }
  .info-text strong { color: var(--ink); font-weight: 600; }
  .or-tag {
    position: absolute; left: 229px; top: 923px; width: 96px; height: 22px;
    background: var(--ink); transform: skewX(-18deg);
    display: flex; align-items: center; justify-content: center;
  }
  .or-tag span { transform: skewX(18deg); color: var(--sun); font-weight: 700; font-size: 17px; }
  .contact { position: absolute; left: 76px; top: 943px; color: var(--paper); font-family: "League Spartan", sans-serif; font-weight: 700; font-size: 27px; line-height: 34px; }
  .email { display: flex; align-items: center; gap: 12px; margin-top: 2px; font-family: "Lexend", sans-serif; font-weight: 600; font-size: 20px; }
  .email svg { flex: none; }
  .website { position: absolute; left: 72px; top: 1134px; display: flex; align-items: center; gap: 14px; color: var(--ink); font-weight: 700; font-size: 23px; }
  .photo { position: absolute; }
  .photo-books { left: 850px; top: 35px; width: 256px; height: 256px; border-radius: 50%;
    background: linear-gradient(180deg, #8f9aa6 0%, #b7bfc6 35%, #7aa63c 52%, #3e4a5a 66%, #e8d83a 82%, #6b6f74 100%); }
  .photo-student { left: 653px; top: 242px; width: 366px; height: 366px; border-radius: 50%;
    background: linear-gradient(160deg, #c9ced6 0%, #9aa3b0 35%, #1d2535 60%, #e9ebef 100%); }
  .photo-group { left: 520px; top: 830px; width: 680px; height: 370px;
    background: linear-gradient(180deg, rgba(170,195,225,0) 0%, rgba(170,195,225,0.85) 25%, #9db4d6 55%, #1b2236 85%, #1b2236 100%);
    border-radius: 160px 160px 0 0; }
</style>
</head>
<body>
<main class="poster">
  <div class="landscape" role="img" aria-label="Aerial view of a winding river through green wetlands and suburbs"></div>

  <svg class="shapes" width="1200" height="1200" viewBox="0 0 1200 1200" aria-hidden="true">
    <path d="M0,0 H798 Q860,30 900,80 L740,380 C600,470 430,545 300,543 C170,541 80,510 0,477 Z" fill="var(--sun)"/>
    <path d="M0,0 H798 Q860,30 890,75 L760,340 C600,430 420,510 300,505 C170,500 80,470 0,443 Z" fill="var(--paper)"/>
    <path d="M0,1100 Q300,1085 520,1075 L520,1200 H0 Z" fill="var(--sun)"/>
    <circle cx="983" cy="160" r="140" fill="none" stroke="var(--sun)" stroke-width="4"/>
    <circle cx="978" cy="163" r="132" fill="none" stroke="var(--paper)" stroke-width="6"/>
    <circle cx="845" cy="430" r="195" fill="none" stroke="var(--sun)" stroke-width="4"/>
    <circle cx="836" cy="425" r="188" fill="none" stroke="var(--paper)" stroke-width="5"/>
    <g fill="var(--bubble)">
      <circle cx="1036" cy="298" r="50"/>
      <circle cx="990" cy="285" r="24"/>
      <circle cx="680" cy="550" r="50"/>
      <circle cx="650" cy="490" r="28"/>
    </g>
    <defs>
      <linearGradient id="infoFade" x1="0" y1="0" x2="0" y2="1">
        <stop offset="0" stop-color="#ffffff"/>
        <stop offset="0.6" stop-color="#ffffff"/>
        <stop offset="1" stop-color="#ffe600"/>
      </linearGradient>
    </defs>
    <polygon points="45,797 436,797 505,860 453,935 45,935" fill="url(#infoFade)"/>
    <line x1="45" y1="937" x2="455" y2="937" stroke="var(--ink)" stroke-width="3"/>
    <path d="M330,932 C400,930 420,960 375,970" fill="none" stroke="var(--paper)" stroke-width="3"/>
    <path d="M385,962 L372,970 L384,978" fill="none" stroke="var(--paper)" stroke-width="3" stroke-linecap="round"/>
  </svg>

  <div class="photo photo-books" role="img" aria-label="Stack of science textbooks beside a school uniform"></div>
  <div class="photo photo-student" role="img" aria-label="Student in uniform writing at a desk in a classroom"></div>
  <div class="photo photo-group" role="img" aria-label="Group of six students in school uniform standing together"></div>

  <div class="school-name"><span class="dot"></span>Harlow Vale</div>

  <div class="year">2022</div>
  <h1 class="title">
    <span class="line-1">SUMMIT SCHOLARS</span>
    <span class="line-2">ADVANCEMENT</span>
    <span class="line-3">PROGRAM</span>
  </h1>

  <p class="lead">The Summit Scholars Advancement<br>Program is a <em>differentiated pathway</em><br>that caters specifically <em>for highly capable students.</em></p>

  <p class="detail">In the Summit Scholars Advancement Pathway, <em>students can learn and be assessed at a pace</em> exceeding that of their current year level, with a focus on 21st Century Skills.</p>

  <p class="info-text">For information about the program<br>and application packages,<br>please see the <strong>summit page of</strong><br><strong>our website</strong></p>

  <div class="or-tag"><span>OR</span></div>

  <div class="contact">
    <p>contact</p>
    <p>Megan Tolland Head of</p>
    <p>Department Junior School</p>
    <p class="email">
      <svg width="26" height="26" viewBox="0 0 26 26"><circle cx="13" cy="13" r="12" fill="var(--paper)"/><rect x="6" y="8" width="14" height="10" rx="1" fill="none" stroke="var(--ink)" stroke-width="1.8"/><path d="M6,8 L13,14 L20,8" fill="none" stroke="var(--ink)" stroke-width="1.8"/></svg>
      mtoll41@schoolnet-example.edu.au
    </p>
  </div>

  <p class="website">
    <svg width="22" height="22" viewBox="0 0 22 22" fill="none" stroke="var(--ink)" stroke-width="2"><circle cx="11" cy="11" r="9"/><ellipse cx="11" cy="11" rx="4" ry="9"/><line x1="2" y1="11" x2="20" y2="11"/></svg>
    harlowvale.example.edu.au
  </p>
</main>
</body>
</html>
```